Real Estate Flyer (Brantwell Property)

We need a color CMYK high resolution, print quality horizontal real estate property flyer designed in the sizes of 10" wide and 6.7425" tall and another one in 11" wide and 8.5" tall.
Ad should be professionally looking to U.S. standards. It should be sleek, modern yet classy.
We uploaded in Briefs logo files, agent photo, 2 photos of the property (Must use both) and a sample of a flyer for Maple Crane Luxury Residence. We like how the overlay atop the first photo in the Maple Crane flyer with the company logo in the overlay. We'd like to incorporate that with our logo, the background color of the overlay should match that of our logo. DON'T CHANGE LOGO COLORS. Only use two colors in ad (exact logo blue color and white). The text in the overlay must be "FOR SALE - Potential Income Producing Commercial Office Building". Other details that should be prominent underneath are "42 Havelock Dr., Schaumburg, IL 60177 - Asking Price: $650,000".
Add "Residential & Commercial" under our company logo in italic font.
Add in flyer: "Located seconds away from the Tunbridge Rd. & Pellham Rd. Intersection"
Add in flyer:
- Completely vacant
- 10,000 sq. ft. building
- 55 Car Parking
- 1.38 acre lot
- Over 20 offices and 5 bathrooms.
- Lease out individual office spaces for great monthly cash flow
Put agent's photo and following details professionally displayed:
Dev Okafor
Managing Broker
847-555-0143
dev.okafor@qlmtestates.example
Add from Briefs fair housing logo and PLX logo near agent's information. Logos should be small but yet visible to understand text.
Add at bottom of the ad with separation near agent details:
Looking to Buy or Sell?
I’m your one-stop, full service licensed real estate broker.
I deal with all types of real estate properties: Homes, Condos, Townhomes, Multi-Unit Apartment Buildings and Commercial Spaces.
Let My Experience Guide You Through Every Step of the Process!
Fine print:
©2018 QLMT Estates, Inc. All Rights Reserved.

```html
<!DOCTYPE html>
<html lang="en">
<head>
<meta charset="utf-8">
<title>Brantwell Property – For Sale Flyer</title>
<link rel="stylesheet" href="https://fonts.googleapis.com/css2?family=Bangers&family=Lato:ital,wght@0,300;0,400;0,700;1,400;1,700&display=swap">
<style>
  :root {
    --brand-blue: #0b4aa6;
    --white: #ffffff;
    --ink: #1a1a1a;
    --paper: #f2f2f2;
    --backdrop: #e4e4e4;
  }
  * { margin: 0; padding: 0; box-sizing: border-box; }
  html, body { width: 1200px; height: 1200px; overflow: hidden; }
  body { background: var(--backdrop); font-family: "Lato", sans-serif; color: var(--ink); position: relative; }

  .flyer {
    position: absolute; left: 20px; top: 180px; width: 1160px; height: 840px;
    background: linear-gradient(180deg, var(--white) 0%, var(--paper) 100%);
    overflow: hidden;
  }
  .hero-photo {
    position: absolute; left: 0; top: 0; width: 684px; height: 400px;
    background: linear-gradient(180deg, #9fb7d2 0%, #d9c9a8 45%, #8b7f6c 62%, #2a2a2c 100%);
  }
  .location-note {
    position: absolute; left: 0; top: 400px; width: 684px; height: 40px;
    display: flex; align-items: center; justify-content: center;
    font-size: 15px; font-weight: 700; color: var(--ink);
  }

  .overlay {
    position: absolute; left: 684px; top: 0; width: 476px; height: 440px;
    background: var(--brand-blue); color: var(--white); text-align: center;
  }
  .brand { position: absolute; top: 62px; left: 0; width: 100%; }
  .brand-name {
    display: inline-flex; align-items: center; gap: 10px;
    font-size: 40px; font-weight: 700; letter-spacing: 1px;
  }
  .brand-name .mark { width: 18px; height: 18px; background: var(--white); }
  .brand-tagline { font-size: 12px; font-style: italic; font-weight: 700; margin-top: 6px; }
  .sale-title {
    position: absolute; top: 166px; left: 0; width: 100%;
    font-family: "Bangers", sans-serif; font-size: 86px; line-height: 1; letter-spacing: 3px;
  }
  .sale-subtitle {
    position: absolute; top: 264px; left: 0; width: 100%;
    font-size: 22px; line-height: 26px; text-transform: uppercase;
  }
  .overlay-rule { position: absolute; top: 328px; left: 54px; width: 358px; height: 1px; background: var(--white); }
  .address { position: absolute; top: 344px; left: 0; width: 100%; font-size: 21px; }
  .price { position: absolute; top: 382px; left: 0; width: 100%; font-size: 34px; }
  .price strong { font-weight: 700; }

  .features { position: absolute; left: 44px; top: 460px; width: 330px; list-style: none; }
  .features li {
    position: relative; padding-left: 40px; font-size: 25px; font-weight: 300;
    line-height: 22px; margin-bottom: 20px; white-space: nowrap;
  }
  .features li svg { position: absolute; left: 3px; top: 2px; }

  .gallery-photo { position: absolute; left: 370px; width: 306px; height: 171px; }
  .gallery-photo.lot { top: 457px; background: linear-gradient(180deg, #a9b3b9 0%, #7d7a6c 35%, #2d2f33 60%, #1e2024 100%); }
  .gallery-photo.street { top: 632px; background: linear-gradient(180deg, #b8bfc6 0%, #d4c3a1 42%, #6c6a60 55%, #26272b 100%); }

  .copyright { position: absolute; left: 40px; top: 790px; font-size: 11px; }

  .pitch { position: absolute; left: 704px; top: 462px; width: 420px; }
  .pitch-title { font-family: "Bangers", sans-serif; font-size: 36px; color: var(--brand-blue); letter-spacing: 1px; line-height: 1; }
  .pitch p { font-size: 12.5px; text-decoration: underline; margin-top: 14px; line-height: 16px; }
  .pitch em { font-weight: 700; }

  .agent { position: absolute; left: 680px; top: 640px; width: 280px; text-align: right; }
  .agent-name { font-size: 32px; font-weight: 700; color: var(--brand-blue); line-height: 36px; }
  .agent-title { font-size: 17px; font-weight: 300; }
  .agent-phone { font-size: 18px; font-weight: 700; margin-top: 6px; }
  .agent-email { font-size: 16px; white-space: nowrap; }
  .badges { display: flex; justify-content: flex-end; gap: 16px; margin-top: 8px; }
  .badge-listing { width: 104px; height: 32px; border: 1px solid #555; }
  .badge-housing { width: 40px; height: 30px; background: #222; }
  .agent-photo { position: absolute; left: 976px; top: 642px; width: 132px; height: 142px; background: linear-gradient(180deg, #e6e6e6 0%, #b9b9b9 55%, #1f2328 100%); }
</style>
</head>
<body>
  <main class="flyer">
    <div class="hero-photo" role="img" aria-label="Two-storey office building with dormers beside a parking lot at sunset"></div>
    <p class="location-note">Located seconds away from the Tunbridge Rd. &amp; Pellham Rd. Intersection</p>

    <section class="overlay">
      <div class="brand">
        <div class="brand-name"><span class="mark"></span>QLMT Estates</div>
        <div class="brand-tagline">Residential &amp; Commercial</div>
      </div>
      <h1 class="sale-title">FOR SALE</h1>
      <p class="sale-subtitle">Potential Income Producing<br>Commercial Office Building</p>
      <div class="overlay-rule"></div>
      <p class="address">42 Havelock Dr., Schaumburg, IL 60177</p>
      <p class="price">Asking Price: <strong>$650,000</strong></p>
    </section>

    <ul class="features">
      <li><svg width="18" height="18" viewBox="0 0 18 18"><path d="M2 10 L7 15 L16 2" fill="none" stroke="#0b4aa6" stroke-width="3"/></svg>Completely vacant</li>
      <li><svg width="18" height="18" viewBox="0 0 18 18"><path d="M2 10 L7 15 L16 2" fill="none" stroke="#0b4aa6" stroke-width="3"/></svg>10,000 sq. ft. building</li>
      <li><svg width="18" height="18" viewBox="0 0 18 18"><path d="M2 10 L7 15 L16 2" fill="none" stroke="#0b4aa6" stroke-width="3"/></svg>55 Car Parking</li>
      <li><svg width="18" height="18" viewBox="0 0 18 18"><path d="M2 10 L7 15 L16 2" fill="none" stroke="#0b4aa6" stroke-width="3"/></svg>1.38 acre lot</li>
      <li><svg width="18" height="18" viewBox="0 0 18 18"><path d="M2 10 L7 15 L16 2" fill="none" stroke="#0b4aa6" stroke-width="3"/></svg>Over 20 offices and<br>5 bathrooms.</li>
      <li><svg width="18" height="18" viewBox="0 0 18 18"><path d="M2 10 L7 15 L16 2" fill="none" stroke="#0b4aa6" stroke-width="3"/></svg>Lease out individual<br>office spaces for great<br>monthly cash flow</li>
    </ul>

    <div class="gallery-photo lot" role="img" aria-label="Parking lot with accessible spaces and trees"></div>
    <div class="gallery-photo street" role="img" aria-label="Street view of the office building row"></div>

    <p class="copyright">©2018 QLMT Estates, Inc. All Rights Reserved.</p>

    <section class="pitch">
      <h2 class="pitch-title">LOOKING TO BUY OR SELL?</h2>
      <p>I’m your one-stop, full service licensed real estate broker.</p>
      <p>I deal with all types of real estate properties: <em>Homes, Condos, Townhomes, Multi-Unit Apartment Buildings and Commercial Spaces.</em></p>
      <p>Let My Experience Guide You Through Every Step of the Process!</p>
    </section>

    <section class="agent">
      <div class="agent-name">Dev Okafor</div>
      <div class="agent-title">Managing Broker</div>
      <div class="agent-phone">847-555-0143</div>
      <div class="agent-email">dev.okafor@qlmtestates.example</div>
      <div class="badges">
        <span class="badge-listing"></span>
        <span class="badge-housing"></span>
      </div>
    </section>
    <div class="agent-photo" role="img" aria-label="Portrait of the managing broker in a suit"></div>
  </main>
</body>
</html>
```